KVD Insurance - Letterhead

We need a corporate letterhead template (word) and slide show template (PowerPoint) designed for our Insurance Business.
KVD Insurance is in the insurance industry. Please visit our website www.kvdinsurance-example.com
Both templates (word and PowerPoint) must include the KVD logo (attached to this project) and can be very similar in design.
We are after something creative yet professional in design.
Please feel free to ask any questions.

```html
<!DOCTYPE html>
<html lang="en">
<head>
<meta charset="utf-8">
<title>KVD Insurance – Letterhead</title>
<link rel="stylesheet" href="https://fonts.googleapis.com/css2?family=Open+Sans:wght@400;600&display=swap">
<style>
  :root {
    --page-bg: #e4e5e7;
    --sheet: #ffffff;
    --band-light: #b3e5f7;
    --band-mid: #7fd3f5;
    --ink: #1a1a1a;
    --watermark: #ececec;
    --watermark-dot: #f6e9b8;
  }
  * { margin: 0; padding: 0; box-sizing: border-box; }
  html, body {
    width: 1200px; height: 700px; overflow: hidden;
    background: var(--page-bg);
    font-family: "Open Sans", Arial, sans-serif;
    color: var(--ink);
  }
  .canvas {
    position: relative; width: 1200px; height: 700px;
    display: flex; align-items: center; justify-content: center;
  }
  .letterhead {
    position: relative; width: 600px; height: 700px;
    background: var(--sheet); overflow: hidden;
    box-shadow: 0 4px 18px rgba(0,0,0,.12);
  }
  .header-band {
    position: absolute; left: 0; top: 0; width: 100%; height: 100px;
    background: var(--band-light);
  }
  .date-field {
    position: absolute; left: 35px; top: 37px;
    font-size: 13px; display: flex; align-items: flex-end; gap: 6px;
  }
  .date-line { display: inline-block; width: 115px; border-bottom: 1.5px solid var(--ink); height: 12px; }
  .website { position: absolute; left: 35px; top: 78px; font-size: 13px; }
  .brand-name {
    position: absolute; right: 22px; top: 30px;
    display: flex; align-items: center; gap: 10px;
    font-size: 30px; font-weight: 600; letter-spacing: 1px; line-height: 1;
    white-space: nowrap; color: var(--ink);
  }
  .brand-dot { width: 24px; height: 24px; border-radius: 50%; background: #e8642c; }
  .watermark { position: absolute; left: 0; top: 0; width: 600px; height: 700px; }
  .watermark-dot {
    position: absolute; left: 58px; top: 305px;
    width: 88px; height: 88px; border-radius: 50%; background: var(--watermark-dot);
  }
  .watermark-line {
    position: absolute; white-space: nowrap; line-height: 1;
    font-weight: 400; color: var(--watermark);
  }
  .watermark-line--name { left: 200px; top: 292px; font-size: 96px; letter-spacing: 14px; }
  .watermark-line--sector { left: 62px; top: 398px; font-size: 60px; letter-spacing: 11px; }
  .footer-wave { position: absolute; left: 0; bottom: 0; width: 600px; height: 140px; }
  .contact-block {
    position: absolute; left: 338px; top: 632px;
    font-size: 13px; line-height: 14.5px; list-style: none;
  }
</style>
</head>
<body>
<main class="canvas">
  <article class="letterhead">
    <header class="header-band">
      <p class="date-field">date : <span class="date-line"></span></p>
      <p class="website">www.kvdinsurance-example.com</p>
      <div class="brand-name"><span class="brand-dot"></span>KVD INSURANCE</div>
    </header>

    <div class="watermark" aria-hidden="true">
      <span class="watermark-dot"></span>
      <span class="watermark-line watermark-line--name">KVD</span>
      <span class="watermark-line watermark-line--sector">INSURANCE</span>
    </div>

    <svg class="footer-wave" viewBox="0 0 600 140" aria-hidden="true">
      <path d="M0 140 C 120 60, 330 10, 430 20 C 520 30, 580 90, 600 140 Z" fill="var(--band-light)"/>
      <path d="M0 140 C 130 80, 330 40, 420 45 C 500 52, 560 100, 575 140 Z" fill="var(--band-mid)"/>
    </svg>

    <ul class="contact-block">
      <li>email :</li>
      <li>address :</li>
      <li>tel :</li>
      <li>fax :</li>
    </ul>
  </article>
</main>
</body>
</html>
```